Business Card Design Project

Business card, that is serious, yet elegant/upscale
Using both sides though only one for information
A space for a QR code would be good
basic contact details.
I will upload company logo
Updates

Thanks everyone who has submitted so far.  No additional designs are needed at this time, We could easily select from one of the many that are currebtly shown.

If you have a design in already and it is still listed it is in the running. Do not submit anymore, choosing now is hard enough given the talent and creativity shared.  WE are making a chpice today this evening.

Again thank you all.

Target Market(s)

CIo's, VP's and people at large companies

Industry/Entity Type

Business

Requirements
Must have
• The business card needs the basic ingo like:
The transparent gear/log enlarged on the card has been well received so is now a must forthe wining design

Name
Title

417 W. Ferncourt
#2870
Dunmore,Il 60944
Tel #

contact@brivanto-mail.example
Nice to have
• A QR Code, no glaring, but usable.

Should not have
• no cursive/handwriting fonts.

```html
<!DOCTYPE html>
<html lang="en">
<head>
<meta charset="utf-8">
<title>Corvane Group — Business Card</title>
<link rel="stylesheet" href="https://fonts.googleapis.com/css2?family=Crimson+Text:wght@700&family=Lato:wght@400;700&display=swap">
<style>
  :root {
    --page-bg: #ebe7e1;
    --card-white: #ffffff;
    --card-mist: #f1f1f1;
    --ink-black: #0d0d0d;
    --swoosh-light: #e9eaeb;
    --swoosh-dark: #55585b;
    --brand-green: #41c31d;
    --text-dark: #1b1b1b;
    --text-light: #f4f4f4;
    --rule-grey: #cfcfcf;
  }
  html, body {
    margin: 0;
    padding: 0;
    width: 922px;
    height: 1200px;
    overflow: hidden;
    background: var(--page-bg);
  }
  .canvas {
    position: relative;
    width: 922px;
    height: 1200px;
  }
  .card {
    position: absolute;
    overflow: hidden;
    border-radius: 9px;
    box-shadow: 0 2px 6px rgba(0,0,0,0.18);
  }
  .card-shapes {
    position: absolute;
    inset: 0;
    width: 100%;
    height: 100%;
  }

  /* Vertical company wordmark */
  .side-wordmark {
    position: absolute;
    writing-mode: vertical-rl;
    font-family: "Lato", sans-serif;
    color: var(--text-light);
    line-height: 1;
    margin: 0;
    white-space: nowrap;
  }
  .side-wordmark .company {
    display: block;
    font-size: 34px;
    font-weight: 400;
    letter-spacing: 1.5px;
  }
  .side-wordmark .tagline {
    display: block;
    font-size: 20px;
    letter-spacing: 1.5px;
    margin-right: 8px;
    margin-top: 66px;
  }

  /* Name lockup */
  .brand-lockup {
    position: absolute;
    display: flex;
    align-items: center;
    gap: 12px;
    font-family: "Lato", sans-serif;
    font-weight: 700;
    color: var(--brand-green);
    white-space: nowrap;
  }
  .brand-lockup .brand-dot {
    border-radius: 50%;
    background: var(--brand-green);
    flex: none;
  }

  /* Front card */
  .card-front {
    left: 105px;
    top: 12px;
    width: 780px;
    height: 525px;
    background: var(--card-white);
  }
  .card-front .side-wordmark {
    left: 20px;
    top: 193px;
  }
  .card-front .brand-lockup {
    left: 424px;
    top: 64px;
    font-size: 37px;
  }
  .card-front .brand-dot {
    width: 40px;
    height: 40px;
  }
  .holder-name {
    position: absolute;
    left: 489px;
    top: 158px;
    margin: 0;
    font-family: "Crimson Text", serif;
    font-weight: 700;
    font-size: 34px;
    color: var(--brand-green);
    white-space: nowrap;
  }
  .contact-rule {
    position: absolute;
    left: 446px;
    top: 287px;
    width: 1px;
    height: 222px;
    background: var(--rule-grey);
  }
  .contact-list {
    position: absolute;
    left: 457px;
    top: 330px;
    margin: 0;
    padding: 0;
    list-style: none;
    font-family: "Lato", sans-serif;
    font-weight: 700;
    color: var(--text-dark);
  }
  .contact-item {
    display: flex;
    align-items: center;
    gap: 18px;
    font-size: 17px;
    line-height: 36px;
    white-space: nowrap;
  }
  .contact-item.email {
    margin-top: 12px;
    font-size: 16px;
  }
  .contact-item.phone {
    margin-top: 18px;
  }
  .contact-item .icon {
    width: 52px;
    height: 40px;
    flex: none;
  }

  /* Back card */
  .card-back {
    left: 117px;
    top: 597px;
    width: 759px;
    height: 540px;
    background: radial-gradient(ellipse at 40% 35%, var(--card-white) 0%, var(--card-mist) 100%);
  }
  .card-back .brand-lockup {
    left: 155px;
    top: 192px;
    font-size: 37px;
  }
  .card-back .brand-dot {
    width: 42px;
    height: 42px;
  }
  .card-back .side-wordmark {
    left: 690px;
    top: 80px;
    transform: rotate(180deg);
  }
  .card-back .side-wordmark .company {
    font-size: 35px;
  }
  .qr-note {
    position: absolute;
    left: 29px;
    top: 398px;
    margin: 0;
    font-family: "Crimson Text", serif;
    font-weight: 700;
    font-size: 33px;
    line-height: 40px;
    color: var(--ink-black);
    white-space: nowrap;
  }
</style>
</head>
<body>
<main class="canvas">

  <section class="card card-front" aria-label="Business card front">
    <svg class="card-shapes" viewBox="0 0 780 525" preserveAspectRatio="none" aria-hidden="true">
      <defs>
        <linearGradient id="front-swoosh" x1="0" y1="0" x2="0" y2="1">
          <stop offset="0" stop-color="var(--swoosh-light)"/>
          <stop offset="0.4" stop-color="var(--swoosh-dark)"/>
          <stop offset="1" stop-color="var(--swoosh-dark)"/>
        </linearGradient>
      </defs>
      <path d="M182,75 C330,150 400,300 370,380 C350,440 310,490 275,525 H258 C330,400 330,260 240,130 C215,105 195,88 182,75 Z" fill="url(#front-swoosh)"/>
      <path d="M188,0 C300,90 330,240 300,360 C285,420 265,480 247,525" fill="none" stroke="var(--card-white)" stroke-width="16"/>
      <path d="M0,0 H188 C300,90 330,240 300,360 C285,420 265,480 247,525 H0 Z" fill="var(--ink-black)"/>
    </svg>

    <p class="side-wordmark"><span class="company">CORVANE GROUP</span><span class="tagline">Software Service</span></p>

    <div class="brand-lockup"><span class="brand-dot"></span><span class="brand-name">Corvane Group</span></div>

    <h1 class="holder-name">Your Name Here</h1>

    <div class="contact-rule"></div>
    <ul class="contact-list">
      <li class="contact-item address">
        <svg class="icon" viewBox="0 0 52 40" aria-hidden="true">
          <path d="M26,3 L48,22 H42 V38 H31 V27 H21 V38 H10 V22 H4 Z" fill="var(--ink-black)"/>
        </svg>
        <span>417 W. Ferncourt #2870<br>Dunmore,Il 60944</span>
      </li>
      <li class="contact-item email">
        <svg class="icon" viewBox="0 0 52 40" aria-hidden="true">
          <rect x="6" y="4" width="40" height="32" rx="3" fill="var(--ink-black)"/>
          <rect x="10" y="9" width="32" height="22" fill="none" stroke="var(--card-white)" stroke-width="1.6"/>
          <path d="M10,9 L26,22 L42,9 M10,31 L22,19 M42,31 L30,19" fill="none" stroke="var(--card-white)" stroke-width="1.6"/>
        </svg>
        <span>contact@brivanto-mail.example</span>
      </li>
      <li class="contact-item phone">
        <svg class="icon" viewBox="0 0 52 40" aria-hidden="true">
          <circle cx="24" cy="20" r="17" fill="none" stroke="var(--ink-black)" stroke-width="3"/>
          <path d="M18,11 l4,0 l2,6 l-3,2 c1.5,3 3.5,5 6,6 l2,-3 l6,2 l0,4 c-9,1 -18,-8 -17,-17 z" fill="var(--ink-black)"/>
        </svg>
        <span>01234587102</span>
      </li>
    </ul>
  </section>

  <section class="card card-back" aria-label="Business card back">
    <svg class="card-shapes" viewBox="0 0 759 540" preserveAspectRatio="none" aria-hidden="true">
      <defs>
        <linearGradient id="back-swoosh" x1="0" y1="0" x2="0" y2="1">
          <stop offset="0" stop-color="var(--swoosh-light)"/>
          <stop offset="0.4" stop-color="var(--swoosh-dark)"/>
          <stop offset="1" stop-color="var(--swoosh-dark)"/>
        </linearGradient>
      </defs>
      <path d="M586,82 C520,180 470,300 480,420 C485,470 500,510 510,540 H535 C515,470 500,380 520,260 C535,190 560,130 586,82 Z" fill="url(#back-swoosh)"/>
      <path d="M603,0 C565,120 520,230 535,340 C545,420 558,480 565,540" fill="none" stroke="var(--card-white)" stroke-width="16"/>
      <path d="M603,0 C565,120 520,230 535,340 C545,420 558,480 565,540 H759 V0 Z" fill="var(--ink-black)"/>
    </svg>

    <div class="brand-lockup"><span class="brand-dot"></span><span class="brand-name">Corvane Group</span></div>

    <p class="side-wordmark"><span class="company">CORVANE GROUP</span><span class="tagline">Software Service</span></p>

    <p class="qr-note">Space for your<br>QR code</p>
  </section>

</main>
</body>
</html>
```